Need a business card for our overland brand!

We had the logo made and we need a great design for our business card. Use the logo provide or tweak it however you see fit.

Contact Information for Business Card

Name, Title, Telephone, email, website

```html
<!DOCTYPE html>
<html lang="en">
<head>
<meta charset="utf-8">
<title>Frostline Trails – Business Card</title>
<link href="https://fonts.googleapis.com/css2?family=Source+Sans+3:wght@400;600;700&display=swap" rel="stylesheet">
<style>
  :root {
    --backdrop: #070302;
    --brand-blue: #1ba0c2;
    --ink-navy: #243a52;
    --paper: #ffffff;
    --haze-on-blue: rgba(255,255,255,0.12);
    --haze-on-white: rgba(27,160,194,0.10);
  }
  * { margin: 0; padding: 0; box-sizing: border-box; }
  html, body {
    width: 1200px; height: 1200px; overflow: hidden;
    background: var(--backdrop);
    font-family: "Source Sans 3", sans-serif;
  }
  .canvas { position: relative; width: 1200px; height: 1200px; }

  .card {
    position: absolute; left: 368px; width: 503px; height: 315px;
    border-radius: 40px; overflow: hidden;
  }
  .card--front { top: 266px; background: var(--brand-blue); }
  .card--back { top: 613px; background: var(--paper); }

  .scenery {
    position: absolute;
  }
  .card--front .scenery {
    left: 0; top: 163px; width: 402px; height: 111px;
    background: linear-gradient(180deg, var(--haze-on-blue), rgba(255,255,255,0.04));
  }
  .card--back .scenery {
    left: 30px; top: 68px; width: 469px; height: 157px;
    background: linear-gradient(180deg, var(--haze-on-white), rgba(27,160,194,0.03));
  }

  .wordmark {
    position: absolute; text-align: center;
    font-weight: 700; line-height: 1.05; letter-spacing: 0.3px;
    text-transform: uppercase;
  }
  .card--front .wordmark {
    left: 0; width: 494px; top: 106px; font-size: 43px; color: var(--paper);
  }
  .card--back .wordmark {
    left: 20px; width: 206px; top: 116px; font-size: 31px; color: var(--ink-navy);
  }

  .divider {
    position: absolute; left: 246px; top: 76px; width: 2px; height: 158px;
    background: var(--brand-blue);
  }

  .identity {
    position: absolute; right: 39px; top: 66px; text-align: right;
    color: var(--ink-navy);
  }
  .identity__name { font-size: 27px; font-weight: 600; line-height: 1; }
  .identity__title { font-size: 22px; font-weight: 600; line-height: 1; margin-top: 1px; }
  .identity-tab {
    position: absolute; right: 0; top: 66px; width: 25px; height: 43px;
    background: var(--brand-blue);
  }

  .contacts {
    position: absolute; right: 19px; top: 175px; list-style: none;
    color: var(--ink-navy); font-size: 14px;
  }
  .contacts li {
    display: flex; align-items: center; justify-content: flex-end;
    height: 18.5px; gap: 8px;
  }
  .contacts svg { width: 12px; height: 12px; flex: none; }

  .address-band {
    position: absolute; left: 0; bottom: 0; width: 503px; height: 39px;
    background: var(--brand-blue); color: var(--ink-navy);
    font-size: 18.5px; font-weight: 600;
    display: flex; align-items: center; justify-content: center;
    padding-right: 6px;
  }
</style>
</head>
<body>
<main class="canvas">

  <section class="card card--front" aria-label="Card front">
    <div class="scenery" role="img" aria-label="Faint mountain range illustration"></div>
    <div class="wordmark">Frostline<br>Trails</div>
  </section>

  <section class="card card--back" aria-label="Card back">
    <div class="scenery" role="img" aria-label="Faint mountain range illustration"></div>
    <div class="wordmark">Frostline<br>Trails</div>
    <div class="divider"></div>

    <div class="identity">
      <p class="identity__name">Lukas BRENNER</p>
      <p class="identity__title">Director</p>
    </div>
    <div class="identity-tab"></div>

    <ul class="contacts">
      <li>+41 70 555 12 34
        <svg viewBox="0 0 24 24" aria-hidden="true"><path fill="#1ba0c2" d="M6.6 10.8a15.1 15.1 0 0 0 6.6 6.6l2.2-2.2a1 1 0 0 1 1-.25 11.4 11.4 0 0 0 3.6.57 1 1 0 0 1 1 1V20a1 1 0 0 1-1 1A17 17 0 0 1 3 4a1 1 0 0 1 1-1h3.5a1 1 0 0 1 1 1c0 1.25.2 2.450.57 3.57a1 1 0 0 1-.25 1z"/></svg>
      </li>
      <li>lukas@frostlinetrails.com
        <svg viewBox="0 0 24 24" aria-hidden="true" fill="none" stroke="#1ba0c2" stroke-width="1.8"><rect x="2" y="5" width="20" height="14" rx="1"/><path d="M2 5l10 8 10-8M2 19l7-6M22 19l-7-6"/></svg>
      </li>
      <li>www.frostlinetrails.com
        <svg viewBox="0 0 24 24" aria-hidden="true" fill="none" stroke="#1ba0c2" stroke-width="1.6"><circle cx="12" cy="12" r="9.5"/><ellipse cx="12" cy="12" rx="4" ry="9.5"/><path d="M2.5 12h19M4 7h16M4 17h16"/></svg>
      </li>
    </ul>

    <div class="address-band">12, Street Name,1203 House, State Name</div>
  </section>

</main>
</body>
</html>
```